Business Card Design Project for Female Personal Trainer

I need a business card design to appeal to female clients for my personal training and group fitness boot camp business called 'LumaStride Studio'. It should be girly, fun and have an active/healthy pic or figure incorporated into the business name.

Target Market(s)

- Females 20-65yrs

Industry/Entity Type

Training

Font styles to use
Serif
Sans Serif

Colors
e34197
e567a6

Requirements
Must have
• First Side of Business Card Details :

Odette Calvo
MASTER PERSONAL TRAINER
Cert III & Cert IV in Fitness
Senior First Aid
Mobile: 0493 507 618
Email: lumastride@quellmail.test
Facebook: LumaStride Studio

* Mobile Personal Training *Individual Sessions *Bootcamp *Weight-loss and Toning

Second Side of Business Card I want to offer a free personal consult:
Something like this:

Need direction with your health & fitness goals?

Call now for your free 1 on 1 Personal Training Session with full consultation

Nice to have
• Have a sub-heading for example:

'Promoting healthy living through fitness & nutrition'

- have the colour pink or blue (to appeal to a female)

- a picture/motif//logo attached (sometimes a picture paints a thousand words)

Should not have
• * picture of a person with big muscles or appeal to a man (I'm training women only)

* should not be busy or crammed up look (if I've added to much info above please just use to your discretion).

```html
<!DOCTYPE html>
<html lang="en">
<head>
<meta charset="utf-8">
<title>LumaStride Studio – Business Card</title>
<link rel="stylesheet" href="https://fonts.googleapis.com/css2?family=Cinzel:wght@400;700;900&family=Allura&family=PT+Sans:wght@400;700&display=swap">
<style>
  :root {
    --plum: #6e1446;
    --deep-pink: #a8236b;
    --pink: #e34197;
    --soft-pink: #e567a6;
    --blush: #fde3f0;
    --ink: #9c1f62;
    --rule: #111111;
    --paper: #ffffff;
  }
  * { margin: 0; padding: 0; box-sizing: border-box; }
  html, body { width: 884px; height: 1200px; overflow: hidden; background: var(--paper); }
  .sheet { position: relative; width: 884px; height: 1200px; }

  .side-label {
    position: absolute; left: 0; width: 884px; text-align: center;
    font-family: "Cinzel", serif; font-weight: 700; font-size: 46px; color: var(--rule);
  }
  .side-label--front { top: 12px; }
  .side-label--back { top: 1128px; }

  .rule { position: absolute; left: 0; width: 884px; background: var(--rule); }

  .card { position: absolute; left: 0; width: 884px; overflow: hidden; background: var(--paper); }
  .card--front { top: 84px; height: 512px; }
  .card--back { top: 607px; height: 503px; }
  .card__bg { position: absolute; inset: 0; width: 100%; height: 100%; }
  .abs { position: absolute; }

  /* Front */
  .brand { left: 30px; top: 26px; display: flex; align-items: center; gap: 16px; }
  .brand-figure {
    width: 74px; height: 74px; border-radius: 50%; flex: none;
    background: radial-gradient(circle at 40% 35%, var(--blush), var(--soft-pink));
  }
  .brand-name {
    font-family: "Cinzel", serif; font-weight: 900; font-size: 52px; line-height: 60px;
    color: var(--plum);
  }
  .tagline {
    right: 390px; top: 188px; text-align: right;
    font-family: "PT Sans", sans-serif; font-size: 19px; line-height: 27px; color: var(--paper);
  }
  .service-list { left: 28px; top: 258px; list-style: none; }
  .service-list li {
    font-family: "Cinzel", serif; font-weight: 700; font-size: 24.5px; line-height: 31.5px;
    color: var(--blush); text-shadow: 1px 2px 2px rgba(70,0,35,.7); white-space: nowrap;
  }
  .service-list li::before { content: "• "; }

  .trainer-name {
    left: 520px; top: 84px; width: 350px; text-align: center;
    font-family: "Allura", cursive; font-size: 92px; line-height: 70px; color: var(--pink);
  }
  .trainer-role {
    left: 560px; top: 236px; width: 314px; text-align: right; padding-right: 34px;
    font-family: "PT Sans", sans-serif; font-weight: 700; font-size: 18px; color: var(--ink); text-transform: uppercase;
  }
  .credentials, .contact {
    right: 34px; text-align: right;
    font-family: "PT Sans", sans-serif; font-size: 18px; color: var(--ink);
  }
  .credentials { top: 274px; line-height: 38px; }
  .contact { top: 396px; line-height: 27.5px; }

  /* Back */
  .offer-heading {
    left: 10px; top: 60px; width: 446px; text-align: center;
    font-family: "Cinzel", serif; font-weight: 700; font-size: 38px; line-height: 51px;
    color: var(--deep-pink); text-shadow: 1px 1px 2px rgba(100,10,50,.35);
  }
  .offer-call {
    left: 10px; top: 318px; width: 446px; text-align: center;
    font-family: "Cinzel", serif; font-weight: 700; font-size: 25px; line-height: 33.5px;
    color: var(--pink); text-shadow: 1px 1px 1px rgba(100,10,50,.3);
  }
  .programs-title {
    left: 500px; top: 38px; width: 370px; text-align: center;
    font-family: "Allura", cursive; font-size: 76px; line-height: 58px; color: var(--paper);
  }
  .programs-rule { left: 520px; top: 164px; width: 330px; height: 2px; background: var(--paper); }
  .program-list { left: 500px; top: 186px; width: 370px; list-style: none; text-align: center; }
  .program-list li {
    font-family: "Cinzel", serif; font-weight: 700; font-size: 26px; line-height: 31px; color: var(--paper);
    margin-bottom: 19px; text-shadow: 1px 1px 2px rgba(70,0,35,.4);
  }
</style>
</head>
<body>
<main class="sheet">
  <p class="side-label side-label--front">FRONT</p>
  <div class="rule" style="top:79px;height:4px"></div>

  <section class="card card--front" aria-label="Business card front">
    <svg class="card__bg" viewBox="0 0 884 512" preserveAspectRatio="none" aria-hidden="true">
      <defs>
        <linearGradient id="frontPink" x1="0" y1="0" x2="0" y2="1">
          <stop offset="0" style="stop-color:var(--soft-pink)"/>
          <stop offset="0.55" style="stop-color:var(--pink)"/>
          <stop offset="1" style="stop-color:var(--deep-pink)"/>
        </linearGradient>
      </defs>
      <path d="M0 0H566 C498 140 488 330 580 512 H0Z" style="fill:var(--soft-pink)"/>
      <path d="M0 0H548 C480 140 470 330 562 512 H0Z" fill="url(#frontPink)"/>
    </svg>

    <div class="abs brand">
      <div class="brand-figure" role="img" aria-label="Active female figure motif"></div>
      <h1 class="brand-name">LumaStride<br>Studio</h1>
    </div>
    <p class="abs tagline">Promoting healthy living through<br>fitness &amp; nutrition</p>
    <ul class="abs service-list">
      <li>Mobile Personal Training</li>
      <li>Group Sessions</li>
      <li>Bootcamp</li>
      <li>Individual Sessions</li>
      <li>Boxing for strength and fitness</li>
      <li>Weight-loss and Toning</li>
      <li>General Fitness</li>
    </ul>

    <h2 class="abs trainer-name">Odette<br>Calvo</h2>
    <p class="abs trainer-role">Master Personal Trainer</p>
    <p class="abs credentials">Cert III &amp; Cert IV in Fitness<br>Senior First Aid</p>
    <p class="abs contact">Mobile: 0493 507 618<br>Email: lumastride@quellmail.test<br>Facebook: LumaStride Studio</p>
  </section>

  <div class="rule" style="top:596px;height:4px"></div>
  <div class="rule" style="top:603px;height:3px"></div>

  <section class="card card--back" aria-label="Business card back">
    <svg class="card__bg" viewBox="0 0 884 503" preserveAspectRatio="none" aria-hidden="true">
      <defs>
        <linearGradient id="backPink" x1="0" y1="0" x2="0" y2="1">
          <stop offset="0" style="stop-color:var(--deep-pink)"/>
          <stop offset="0.5" style="stop-color:var(--pink)"/>
          <stop offset="1" style="stop-color:var(--soft-pink)"/>
        </linearGradient>
      </defs>
      <path d="M884 0H462 C430 160 432 360 500 503 H884Z" style="fill:var(--deep-pink)"/>
      <path d="M884 0H476 C444 160 446 360 514 503 H884Z" fill="url(#backPink)"/>
    </svg>

    <h2 class="abs offer-heading">Need direction<br>with your<br>health &amp; fitness<br>goals?</h2>
    <p class="abs offer-call">Call now for your<br>free 1 on 1 Personal<br>Training Session<br>with full consultation!</p>

    <h3 class="abs programs-title">Fitness<br>Programs</h3>
    <div class="abs programs-rule"></div>
    <ul class="abs program-list">
      <li>Weight Loss<br>Consults</li>
      <li>Female Specific<br>Training</li>
      <li>Body Sculpting</li>
      <li>HIIT</li>
      <li>Pre/Post Natal</li>
    </ul>
  </section>

  <div class="rule" style="top:1110px;height:4px"></div>
  <p class="side-label side-label--back">BACK</p>
</main>
</body>
</html>
```